Business Card Design - Furniture Retail

Open to both Single or double sided design

We are launching a online ecommerce store that sells Scandinavian/Danish style of furniture in Australia.

We aspire to provide stylish but classic and designers' selection of furniture to the Australia public at affordable price. For the style of the furniture we are selling, please see the following links:

https://www.filecrate.example/sh/qk3mzr8wlp/BXTpLnR4vQ7cYdHs?dl=0

The style of the design we are looking for is clean, simple that look Scandinavian/Danish but yet it is timeless classic.

Aspiring Design
http://www.lindmora.com
http://tobyquell.com.au/
http://vekt.furniture/
http://www.olvo.com/
Updates

Please display the card on normal angle for both front and back instead of funny angle. Please keep it display when displaying the design of the business cards so that we can focus on the designs rather than being confused by the unnecessary stuffs like the hands or background

I think there is already enough curve line on the logo itself so anything extra of the curve on the business card would be really unnecessary. Please avoid using any of the extra curve line on the business card, other than the logo itself. Thanks

Regular card and give them a matt celloglaze to create texture on card that makes it looked luxury and expensive.

Please display design on normal angle! Please only use white colour in the background (not the business card but the referring to the submission) rather than anything fancy so that we can focus on the design.

Target Market(s)

High end market consumers who are financially capable and who has good taste and appreciate good design

aged between 28 - 45 white collars professional/businessmen who live in metropolitan areas

Industry/Entity Type

Business

Font styles to use
Serif
Sans Serif

Requirements
Must have
• Regular card and give them a matt celloglaze to create texture on card that makes it looked luxury and expensive.

Please use the logo from the uploaded files

Company Name: Milo Verhagen
Name: Milo Reeb
Phone: +614 27 305 641
Website: www.miloverhagen.com.au
Email: milo@miloverhagen.com.au
Nice to have
• Colour is not limited to black and white
Should not have
• The concept photos of the furniture should NOT be used in the FRONT page of the business card.

```html
<!DOCTYPE html>
<html lang="en">
<head>
<meta charset="utf-8">
<title>Milo Verhagen — Business Card</title>
<link rel="stylesheet" href="https://fonts.googleapis.com/css2?family=PT+Serif:wght@400&display=swap">
<style>
  :root {
    --page-bg: #ffffff;
    --card-black: #0b0b0b;
    --card-sheen: #2a2a2a;
    --ink-light: #f2f2f2;
    --ink-soft: #d9d9d9;
    --rule: #e6e6e6;
    --band-top: #f4f4f4;
    --band-bottom: #c9c9c9;
    --band-ink: #2b2b2b;
  }
  html, body {
    margin: 0;
    padding: 0;
    width: 1200px;
    height: 992px;
    overflow: hidden;
    background: var(--page-bg);
  }
  .canvas {
    width: 1200px;
    height: 992px;
    display: flex;
    align-items: center;
    justify-content: center;
  }
  .business-card {
    position: relative;
    width: 900px;
    height: 514px;
    background:
      radial-gradient(ellipse 70% 90% at 35% 55%, var(--card-sheen) 0%, var(--card-black) 70%);
    box-shadow: 0 10px 30px rgba(0,0,0,0.18);
    font-family: "PT Serif", Georgia, serif;
    color: var(--ink-light);
    overflow: hidden;
  }
  .brand-name {
    position: absolute;
    left: 56px;
    top: 118px;
    margin: 0;
    font-size: 66px;
    font-weight: 400;
    letter-spacing: 2px;
    text-transform: uppercase;
    color: var(--ink-light);
    line-height: 1;
  }
  .name-rule {
    position: absolute;
    top: 224px;
    left: 0;
    right: 0;
    display: flex;
    align-items: center;
    gap: 18px;
  }
  .name-rule .line-long {
    flex: 1;
    height: 2px;
    background: var(--rule);
  }
  .name-rule .line-short {
    width: 44px;
    height: 2px;
    background: var(--rule);
  }
  .person-name {
    font-size: 24px;
    color: var(--ink-light);
    white-space: nowrap;
  }
  .contact-list {
    position: absolute;
    right: 44px;
    top: 268px;
    margin: 0;
    padding: 0;
    list-style: none;
    text-align: right;
  }
  .contact-list li {
    display: flex;
    justify-content: flex-end;
    align-items: center;
    gap: 14px;
    font-size: 22px;
    color: var(--ink-soft);
    margin-bottom: 18px;
  }
  .contact-list svg {
    width: 18px;
    height: 18px;
    fill: var(--ink-soft);
  }
  .web-band {
    position: absolute;
    left: 0;
    right: 0;
    bottom: 0;
    height: 92px;
    background: linear-gradient(180deg, var(--band-top), var(--band-bottom));
    display: flex;
    align-items: center;
    padding-left: 250px;
    box-sizing: border-box;
  }
  .web-address {
    font-size: 28px;
    letter-spacing: 0.5px;
    color: var(--band-ink);
  }
</style>
</head>
<body>
  <main class="canvas">
    <section class="business-card" aria-label="Milo Verhagen business card">
      <h1 class="brand-name">Milo Verhagen</h1>

      <div class="name-rule">
        <span class="line-long"></span>
        <span class="person-name">Milo Reeb</span>
        <span class="line-short"></span>
      </div>

      <ul class="contact-list">
        <li>
          <span class="phone">+614 27 305 641</span>
          <svg viewBox="0 0 24 24" aria-hidden="true"><path d="M6.6 10.8a15.1 15.1 0 0 0 6.6 6.6l2.2-2.2c.3-.3.7-.4 1-.2 1.1.4 2.3.6 3.6.6.6 0 1 .4 1 1V20c0 .6-.4 1-1 1C10.6 21 3 13.4 3 4c0-.6.4-1 1-1h3.5c.6 0 1 .4 1 1 0 1.3.2 2.5.6 3.6.1.3 0 .7-.2 1z"/></svg>
        </li>
        <li>
          <span class="email">milo@miloverhagen.com.au</span>
          <svg viewBox="0 0 24 24" aria-hidden="true"><path d="M2 5h20v14H2z M3.5 6.5 12 13l8.5-6.5" fill="none" stroke="#d9d9d9" stroke-width="1.8"/><path d="M2 5h20L12 12.5z"/></svg>
        </li>
      </ul>

      <div class="web-band">
        <span class="web-address">www.miloverhagen.com.au</span>
      </div>
    </section>
  </main>
</body>
</html>
```